FotoVELTA buisnesscard

Hey :) I need a modern buisnesscard for my company FotoVELTA
It most have:
Dagligleder og Fotograf: Henrik Torvald Bjelland

Mob: +4791642058
Epost: post@fotovelta.no
Adresse: Bakkestien22, 4417 Fjellvika

Facbook and instagram logo with text FotoVELTA

FotoVELTA logo

It Company

```html
<!DOCTYPE html>
<html lang="no">
<head>
<meta charset="utf-8">
<title>FotoVELTA – visittkort</title>
<link rel="stylesheet" href="https://fonts.googleapis.com/css2?family=Open+Sans:wght@400;600;700;800&display=swap">
<style>
  :root {
    --backdrop: #2b2a2f;
    --card: #151517;
    --silver: #cfcfd1;
    --ink-muted: #4d4d52;
    --ink-soft: #8a8a8f;
    --rule: #333337;
  }
  * { box-sizing: border-box; margin: 0; padding: 0; }
  html, body {
    width: 1200px;
    height: 1050px;
    overflow: hidden;
    background: var(--backdrop);
    font-family: "Open Sans", Arial, sans-serif;
  }
  .sheet {
    width: 1200px;
    height: 1050px;
    display: flex;
    flex-direction: column;
    align-items: center;
    justify-content: center;
    gap: 40px;
  }
  .card {
    position: relative;
    width: 840px;
    height: 480px;
    background: var(--card);
    overflow: hidden;
  }

  /* Front side */
  .holder {
    position: absolute;
    left: 48px;
    top: 44px;
    width: 300px;
  }
  .holder-name {
    color: var(--ink-muted);
    font-size: 30px;
    font-weight: 700;
    line-height: 1.15;
  }
  .holder-title {
    margin-top: 8px;
    padding-bottom: 14px;
    border-bottom: 1px solid var(--rule);
    color: var(--ink-soft);
    font-size: 12px;
    font-weight: 700;
    letter-spacing: 0.04em;
    text-transform: uppercase;
  }
  .contact-list {
    list-style: none;
    margin-top: 18px;
  }
  .contact-item {
    display: flex;
    align-items: flex-start;
    gap: 16px;
    padding: 9px 0;
    border-bottom: 1px solid var(--rule);
    color: var(--ink-soft);
    font-size: 16px;
    line-height: 1.35;
  }
  .contact-item:last-child { border-bottom: none; }
  .contact-icon {
    flex: none;
    width: 16px;
    height: 16px;
    margin-top: 2px;
    fill: none;
    stroke: var(--ink-muted);
    stroke-width: 1.6;
    stroke-linecap: round;
    stroke-linejoin: round;
  }
  .social {
    position: absolute;
    left: 470px;
    top: 64px;
    display: flex;
    align-items: center;
    gap: 12px;
    color: var(--ink-soft);
    font-size: 16px;
    font-weight: 600;
  }
  .social-dot {
    width: 14px;
    height: 14px;
    border-radius: 50%;
    border: 2px solid var(--ink-muted);
  }
  .front-brand {
    position: absolute;
    right: 40px;
    bottom: 44px;
    color: var(--silver);
    font-size: 96px;
    font-weight: 800;
    letter-spacing: -0.02em;
    line-height: 1;
  }

  /* Back side */
  .card-back {
    display: flex;
    align-items: center;
    justify-content: center;
    gap: 26px;
  }
  .back-mark {
    width: 70px;
    height: 70px;
    background: var(--silver);
  }
  .back-brand {
    color: var(--silver);
    font-size: 96px;
    font-weight: 800;
    letter-spacing: -0.02em;
    line-height: 1;
  }
</style>
</head>
<body>
<main class="sheet">
  <section class="card card-front" aria-label="Visittkort forside">
    <div class="holder">
      <h1 class="holder-name">Henrik Torvald<br>Bjelland</h1>
      <p class="holder-title">Daglig leder og fotograf</p>
      <ul class="contact-list">
        <li class="contact-item">
          <svg class="contact-icon" viewBox="0 0 16 16" aria-hidden="true"><path d="M3 1.5h3l1.2 3.2-1.8 1.2a8 8 0 0 0 4.7 4.7l1.2-1.8 3.2 1.2v3a1.5 1.5 0 0 1-1.6 1.5A12.5 12.5 0 0 1 1.5 3.1 1.5 1.5 0 0 1 3 1.5z"/></svg>
          <span>+4791642058</span>
        </li>
        <li class="contact-item">
          <svg class="contact-icon" viewBox="0 0 16 16" aria-hidden="true"><rect x="1.5" y="3" width="13" height="10" rx="1"/><path d="M1.5 4l6.5 5 6.5-5"/></svg>
          <span>post@fotovelta.no</span>
        </li>
        <li class="contact-item">
          <svg class="contact-icon" viewBox="0 0 16 16" aria-hidden="true"><path d="M8 15s5-5 5-8.5A5 5 0 0 0 3 6.5C3 10 8 15 8 15z"/><circle cx="8" cy="6.5" r="1.8"/></svg>
          <span>Bakkestien22<br>4417 Fjellvika</span>
        </li>
      </ul>
    </div>
    <div class="social">
      <span class="social-dot" aria-hidden="true"></span>
      <span>FotoVELTA</span>
    </div>
    <div class="front-brand">FotoVELTA</div>
  </section>

  <section class="card card-back" aria-label="Visittkort bakside">
    <span class="back-mark" aria-hidden="true"></span>
    <span class="back-brand">FotoVELTA</span>
  </section>
</main>
</body>
</html>
```